A5 Flyer for Window Cleaning Company

2 sided Flyer design required for window cleaning company. One side to include we use traditional and hot water fed pole window cleaning systems, conservatory cleaning, and fascia and soffit cleaning. The other side to be for Gutter cleaning. See the must haves section of project brief for more info. Mixture of some images and text for both sides. ( do not have to use all images supplied). The flyer will be used to promote the business to new residential customers.

Target Market(s)

Private households/new customers

Industry/Entity Type

Window Cleaning

Font styles to use
Serif

Requirements
Must have
• Company address ( 7 Old Pennick Court Harlow Street Edinburgh EH4 9RQ
Phone numbers( 0131 482 7719 0800 061 2287).
Website and email address ( info@falconbright-cleaning.example)
Excellent Customer Service. Competitive prices. Established 1994.
Side 1of flyer = Falconbright Window Cleaning Side 2 of flyer Falconbright Gutter Cleaning.
Nice to have
• Professional look.

```html
<!DOCTYPE html>
<html lang="en">
<head>
<meta charset="utf-8">
<title>Falconbright Window Cleaning – Flyer</title>
<link rel="stylesheet" href="https://fonts.googleapis.com/css2?family=Arimo:wght@700&family=Lato:wght@400;700&display=swap">
<style>
  :root {
    --navy: #0b1f5c;
    --navy-deep: #08184d;
    --sky: #6fa6da;
    --sky-soft: #a9c9ea;
    --grey-light: #f4f4f4;
    --grey-mid: #dcdcdc;
    --ink: #1d1d1d;
    --white: #ffffff;
    --page: #e6e6e6;
  }
  * { margin: 0; padding: 0; box-sizing: border-box; }
  html, body { width: 1200px; height: 902px; overflow: hidden; background: var(--page); }
  .flyer {
    position: absolute; left: 0; top: 23px;
    width: 1200px; height: 856px;
    background: var(--white);
    overflow: hidden;
    font-family: "Lato", Arial, sans-serif;
    color: var(--ink);
  }
  .flyer-shapes { position: absolute; inset: 0; }
  .brand-mark {
    position: absolute; left: 430px; top: 170px; width: 170px;
    text-align: center; color: var(--navy);
    font-family: "Arimo", Arial, sans-serif; font-weight: 700;
  }
  .brand-mark__name { font-size: 19px; letter-spacing: 0.5px; line-height: 1.15; }
  .brand-mark__phone { font-size: 19px; margin-top: 6px; }
  .headline {
    position: absolute; left: 612px; width: 588px; text-align: center;
    font-family: "Arimo", Arial, sans-serif; font-weight: 700;
  }
  .headline__name { top: 74px; font-size: 70px; color: var(--white); letter-spacing: 1px; line-height: 1; }
  .headline__service {
    position: absolute; left: 649px; top: 196px; width: 513px; height: 74px;
    background: var(--navy); color: var(--white);
    font-family: "Arimo", Arial, sans-serif; font-weight: 700;
    font-size: 45px; line-height: 74px; text-align: center;
  }
  .headline__area { top: 284px; font-size: 23px; color: #eef4fb; letter-spacing: 0.5px; }
  .promise {
    position: absolute; left: 110px; top: 344px; width: 370px;
    text-align: center; font-weight: 700; font-size: 21px; line-height: 35px;
  }
  .services { position: absolute; left: 86px; top: 460px; }
  .services__title { font-size: 17px; font-weight: 700; letter-spacing: 0.5px; margin-bottom: 14px; }
  .services__list { list-style: none; }
  .services__list li {
    position: relative; padding-left: 34px; font-size: 16px; line-height: 28px;
  }
  .services__list li::before {
    content: ""; position: absolute; left: 2px; top: 7px;
    width: 14px; height: 14px; border-radius: 50%; background: var(--navy);
  }
  .location {
    position: absolute; left: 700px; top: 588px; width: 410px;
    text-align: center; color: var(--white); font-size: 21px; line-height: 28px;
  }
  .location__pin { display: block; margin: 0 auto 12px; }
  .contact-line {
    position: absolute; left: 404px; top: 740px; width: 780px;
    display: flex; gap: 42px; align-items: center;
    color: var(--white);
    font-family: "Arimo", Arial, sans-serif; font-weight: 700; font-size: 38px;
  }
  .contact-line__item { display: flex; align-items: center; gap: 14px; white-space: nowrap; }
</style>
</head>
<body>
<div class="flyer">
  <svg class="flyer-shapes" width="1200" height="856" viewBox="0 0 1200 856" aria-hidden="false">
    <defs>
      <linearGradient id="greyFade" x1="0" y1="0" x2="1" y2="0">
        <stop offset="0" stop-color="#ffffff"/>
        <stop offset="0.45" stop-color="#f1f1f1"/>
        <stop offset="1" stop-color="#dedede"/>
      </linearGradient>
      <linearGradient id="photoCleaner" x1="0" y1="0" x2="1" y2="1">
        <stop offset="0" stop-color="#dfe6ec"/>
        <stop offset="0.6" stop-color="#9fb3c6"/>
        <stop offset="1" stop-color="#6e7f6a"/>
      </linearGradient>
      <linearGradient id="photoVan" x1="0" y1="0" x2="1" y2="1">
        <stop offset="0" stop-color="#bfe0f6"/>
        <stop offset="0.6" stop-color="#5fb0e4"/>
        <stop offset="1" stop-color="#2e4b70"/>
      </linearGradient>
    </defs>

    <!-- light grey copy panel -->
    <polygon points="0,340 298,304 612,340 612,856 0,856" fill="url(#greyFade)"/>

    <!-- top-left photo area -->
    <polygon role="img" aria-label="Photo of a window cleaner in a blue cap washing a window with a squeegee applicator"
             points="0,0 412,0 412,303 298,290 0,326" fill="url(#photoCleaner)"/>

    <!-- brand square -->
    <rect x="455" y="40" width="120" height="120" fill="var(--sky)"/>

    <!-- headline panel -->
    <polygon points="612,0 1200,0 1200,326 898,356 612,324" fill="var(--sky)"/>

    <!-- chevron band -->
    <polyline points="0,332 298,296 898,364 1200,334" fill="none" stroke="var(--navy)" stroke-width="9"/>

    <!-- photo strip -->
    <polygon role="img" aria-label="Photo of a window cleaner using a squeegee on a large pane"
             points="612,340 793,360 793,558 612,545" fill="#8b8f93"/>
    <polygon role="img" aria-label="Photo of a white conservatory on a red brick house"
             points="798,361 898,372 996,362 996,557 898,566 798,558" fill="#b7a08e"/>
    <polygon role="img" aria-label="Photo of a brush cleaning white fascia and soffits"
             points="1001,362 1200,342 1200,540 1001,557" fill="#d4d6d8"/>

    <!-- lower navy contact panel -->
    <polygon points="612,552 898,574 1200,548 1200,834 370,834 370,714 612,714" fill="var(--navy)"/>

    <!-- van photo -->
    <rect role="img" aria-label="Photo of the company's branded light blue van" x="52" y="612" width="324" height="234" rx="28" fill="url(#photoVan)"/>
  </svg>

  <div class="brand-mark">
    <div class="brand-mark__name">FALCONBRIGHT<br>WINDOW CLEANING</div>
    <div class="brand-mark__phone">0800 061 2287</div>
  </div>

  <div class="headline headline__name">FALCONBRIGHT</div>
  <div class="headline__service">WINDOW CLEANING</div>
  <div class="headline headline__area">EDINBURGH</div>

  <div class="promise">
    <p>Excellent Customer Service.</p>
    <p>Competitive prices.</p>
    <p>Established 1994.</p>
  </div>

  <div class="services">
    <p class="services__title">WE USE</p>
    <ul class="services__list">
      <li>Traditional and hot water fed pole window cleaning systems</li>
      <li>Conservatory cleaning</li>
      <li>Fascia and soffit cleaning</li>
    </ul>
  </div>

  <div class="location">
    <svg class="location__pin" width="22" height="32" viewBox="0 0 22 32" aria-hidden="true">
      <path d="M11 1C5.5 1 1 5.4 1 10.8 1 18 11 30 11 30s10-12 10-19.2C21 5.4 16.5 1 11 1z" fill="none" stroke="#fff" stroke-width="2.4"/>
      <circle cx="11" cy="11" r="3.6" fill="none" stroke="#fff" stroke-width="2.4"/>
      <line x1="4" y1="31" x2="18" y2="31" stroke="#fff" stroke-width="2"/>
    </svg>
    <p>7 Old Pennick Court</p>
    <p>Harlow Street Edinburgh</p>
    <p>EH4 9RQ</p>
  </div>

  <div class="contact-line">
    <div class="contact-line__item">
      <svg width="36" height="26" viewBox="0 0 36 26" aria-hidden="true">
        <path d="M2 8c0-5 32-5 32 0v3h-9V8c-4-2-10-2-14 0v3H2z" fill="#fff"/>
        <path d="M10 12h16l4 12H6z" fill="#fff"/>
        <circle cx="18" cy="18" r="3.4" fill="var(--navy)"/>
      </svg>
      <span>0131 482 7719</span>
    </div>
    <div class="contact-line__item">
      <svg width="36" height="36" viewBox="0 0 36 36" aria-hidden="true">
        <circle cx="18" cy="18" r="16" fill="none" stroke="#fff" stroke-width="2.4"/>
        <path d="M12.5 9.5l3 3.6-1.8 2.2c1.2 2.6 3.2 4.6 5.8 5.9l2.2-1.8 3.6 3-1.8 3c-6.8-.6-12.4-6.2-13-13z" fill="#fff"/>
      </svg>
      <span>0800 061 2287</span>
    </div>
  </div>
</div>
</body>
</html>
```